Ridgemoor Taproom Beer Can Design

Design a beer can for a boutique craft brewery located in Frankston, Victoria, AUS.
We have a focus on producing socially approachable beers in an ambient setting. The beer can design should be sophisticated, simple, recognizable and a little playful. The color pallet should be inviting and not too bold. The design should have identifying features that can be interchanged onto different cans for different beer types. The design must be repeatable for other beer varieties, which will each have a unique color. The can should feature black, white and purple (this should be in interchangeable color). The beer can also needs to have our Ridgemoor Taproom company logo on it, this has been attached to the design brief.

Target Market(s)

The target market is aged 25+ who are social, have some disposable income and appreciate good beer, wine and food.
The beers will also be made for distribution, initially to locally to restaurants and cafés and eventually commercially.
Tourists will also be targeted due to the area the brewhouse is located (Mornington Peninsula, Victoria, AUS).

Industry/Entity Type

Hospitality

Font styles to use
Sans Serif
Script

Colors
6b449b
876aae
b7a5cd
e4daeb
000000
ffffff
959595

Requirements
Must have
• The ‘Ridgemoor Taproom’ logo.
• The colour associated to this beer - purple. This should be the only colour used on the can (along with black/white/gray).
• The company tagline ‘Socially Approachable’.
• The tasting notes text ‘Bright in colour, dry on the palate and thirst quenching in the extreme, wheat and pale malts compliment each other with nuance.’
• Australian beer can requirements as per 'Requirements.png'. EPS and AI files of the requirements have been included.
Nice to have
• The logo text ‘Cecil Grain IPA’ more predominant than the Ridgemoor Taproom logo.
Should not have
• Be busy, simple is best
• Beer related pictures / images
• Bold, masculine lines and fonts
• Requirements.png directly used. Please use the EPS or AI files provided.

```html
<!DOCTYPE html>
<html lang="en">
<head>
<meta charset="utf-8">
<title>Ridgemoor Taproom — Cecil Grain IPA</title>
<link rel="stylesheet" href="https://fonts.googleapis.com/css2?family=Oswald:wght@400;600&family=Allura&display=swap">
<style>
  :root {
    --purple-deep: #876aae;
    --purple-soft: #b7a5cd;
    --ink: #231f20;
    --black: #000000;
    --white: #ffffff;
  }
  html, body {
    margin: 0;
    padding: 0;
    width: 1200px;
    height: 1200px;
    overflow: hidden;
    background: var(--white);
  }
  .can-label {
    position: relative;
    width: 1200px;
    height: 1200px;
    background: var(--white);
    overflow: hidden;
  }
  .brand-name {
    position: absolute;
    left: 34px;
    top: 34px;
    margin: 0;
    font-family: "Oswald", sans-serif;
    font-weight: 400;
    font-size: 78px;
    line-height: 1.02;
    letter-spacing: 0.12em;
    color: var(--ink);
    text-transform: uppercase;
  }
  .colour-bands {
    position: absolute;
    left: 0;
    top: 0;
    width: 1200px;
    height: 1200px;
  }
  .band-main { fill: var(--purple-deep); }
  .band-shadow { fill: var(--purple-soft); }
  .beer-name {
    position: absolute;
    right: 28px;
    top: 356px;
    margin: 0;
    font-family: "Oswald", sans-serif;
    font-weight: 600;
    font-size: 164px;
    line-height: 1;
    letter-spacing: 0.005em;
    color: var(--white);
    text-transform: uppercase;
    white-space: nowrap;
  }
  .tagline {
    position: absolute;
    left: 40px;
    top: 955px;
    margin: 0;
    font-family: "Allura", cursive;
    font-weight: 400;
    font-size: 118px;
    line-height: 1;
    color: var(--black);
    white-space: nowrap;
  }
  .base-strip {
    position: absolute;
    left: 0;
    bottom: 0;
    width: 1200px;
    height: 62px;
    background: var(--black);
  }
</style>
</head>
<body>
  <main class="can-label">
    <p class="brand-name">Ridgemoor<br>Taproom</p>

    <svg class="colour-bands" viewBox="0 0 1200 1200" aria-hidden="true">
      <polygon class="band-shadow" points="0,684 960,559 1200,647 1200,759 960,703 0,788"/>
      <polygon class="band-main" points="0,341 960,274 1200,304 1200,647 960,559 0,684"/>
    </svg>

    <h1 class="beer-name">Cecil Grain IPA</h1>

    <p class="tagline">Socially Approachable</p>

    <div class="base-strip"></div>
  </main>
</body>
</html>
```